Solar appointment reminder card

We are looking for a new design for our appointment reminder card since we have changed our logo. The card should have the new logo along with space for the employee to hand write the customers appointment date, time, the employees name and phone number.
I've uploaded what our old basic appointment card looked like and our new logo.

The cards should be in a standard business card size and could be horizontal or vertical.

```html
<!DOCTYPE html>
<html lang="en">
<head>
<meta charset="utf-8">
<title>Appointment Reminder Card</title>
<link rel="stylesheet" href="https://fonts.googleapis.com/css2?family=Inter:wght@300;700;800&display=swap">
<style>
  :root {
    --backdrop: #bdbdbf;
    --card-black: #000000;
    --sun-yellow: #fcc729;
    --brand-orange: #f7922a;
    --paper: #ffffff;
    --ink: #111111;
  }
  * { margin: 0; padding: 0; box-sizing: border-box; }
  html, body {
    width: 999px;
    height: 1200px;
    overflow: hidden;
    background: var(--backdrop);
  }
  .card {
    position: absolute;
    left: 199px;
    top: 75px;
    width: 601px;
    height: 1050px;
    background: var(--card-black);
    overflow: hidden;
    font-family: "Inter", "Helvetica Neue", Arial, sans-serif;
  }
  .card-art {
    position: absolute;
    inset: 0;
    width: 601px;
    height: 1050px;
  }
  .brand {
    position: absolute;
    left: 104px;
    top: 95px;
    display: flex;
    align-items: center;
    gap: 22px;
  }
  .brand-dot {
    width: 72px;
    height: 72px;
    border-radius: 50%;
    background: var(--sun-yellow);
    flex: none;
  }
  .brand-name {
    color: var(--brand-orange);
    font-weight: 800;
    font-size: 50px;
    line-height: 52px;
    letter-spacing: -0.5px;
  }
  .appointment {
    position: absolute;
    left: 0;
    right: 0;
    top: 545px;
    text-align: center;
  }
  .appointment-title {
    font-weight: 700;
    font-size: 46px;
    color: var(--ink);
    letter-spacing: -0.3px;
  }
  .fields {
    list-style: none;
    position: absolute;
    left: 62px;
    top: 666px;
  }
  .field {
    font-weight: 300;
    font-size: 31px;
    color: var(--ink);
    height: 93px;
    line-height: 40px;
  }
</style>
</head>
<body>
  <div class="card">
    <svg class="card-art" viewBox="0 0 601 1050" xmlns="http://www.w3.org/2000/svg">
      <defs>
        <linearGradient id="glow" x1="0" y1="0" x2="0" y2="1">
          <stop offset="0" stop-color="#000000"/>
          <stop offset="0.55" stop-color="#c9961c"/>
          <stop offset="1" stop-color="#fcc729"/>
        </linearGradient>
      </defs>
      <rect role="img" aria-label="Decorative sunburst rising behind the appointment panel"
            x="0" y="250" width="601" height="480" fill="url(#glow)"/>
      <path d="M34 720 A267 267 0 0 1 568 720 L601 715 L601 1050 L0 1050 L0 690 Z" fill="var(--paper)"/>
      <ellipse cx="301" cy="725" rx="267" ry="268" fill="var(--paper)"/>
    </svg>

    <div class="brand">
      <span class="brand-dot"></span>
      <span class="brand-name">Empire Sky<br>Solar</span>
    </div>

    <div class="appointment">
      <h1 class="appointment-title">Appointment</h1>
    </div>

    <ul class="fields">
      <li class="field">Date:</li>
      <li class="field">Time:</li>
      <li class="field">Representative:</li>
      <li class="field">Phone:</li>
    </ul>
  </div>
</body>
</html>
```